Music Festival in Colorado Needs Awesome Flier Design

We need an eye-catching & captivating flier design for an annual music festival in Denver, CO (USA). The festival features the best Colorado musicians within the genres of jam - funk - bluegrass - electronic - reggae - rock.

The design should look clean and professional while still being creative and unique. The past three years' flier designs are attached, as well as the logo and some other designs that match the aesthetic of what we're looking for.

This festival has a big element of Colorado pride so any

Target Market(s)

Hippies - live music enthusiasts - partiers. Ages 21 - 40.

Industry/Entity Type

Entertainment

Colors
0355a3
ec1f27
ffffff
fbed22

Requirements
Must have
• Attached design text.
Nice to have
• - Quality texture and psychedelic elements.
• - Colorado pride elements; color scheme (red, white, blue & yellow), flag, ect.
• - Nature elements are awesome but this is also a downtown festival so keep that in mind.
Should not have
• Cheesy artwork.

```html
<!DOCTYPE html>
<html lang="en">
<head>
<meta charset="utf-8">
<title>Pass It Along – Colorado Music Festival Flier</title>
<link href="https://fonts.googleapis.com/css2?family=Oswald:wght@500;700&family=Roboto+Slab:wght@800&family=Montserrat:wght@400;600;700&display=swap" rel="stylesheet">
<style>
  :root {
    --backdrop: #d7dce3;
    --maroon: #6b2117;
    --maroon-dark: #4f170f;
    --teal: #5cc5bf;
    --white: #ffffff;
    --sky-top: #f2f2f2;
    --sky-bottom: #b9b9b9;
  }
  * { margin: 0; padding: 0; box-sizing: border-box; }
  html, body { width: 1200px; height: 800px; overflow: hidden; }
  body { background: var(--backdrop); position: relative; font-family: "Montserrat", sans-serif; }

  .flier {
    position: absolute; left: 330px; top: 18px;
    width: 540px; height: 764px;
    background: var(--maroon);
    overflow: hidden;
    box-shadow: 0 10px 30px rgba(0,0,0,.25);
  }
  .flier__scene {
    position: absolute; left: 0; top: 0; width: 540px; height: 350px;
    background: linear-gradient(180deg, var(--sky-top) 0%, #d6d6d6 55%, var(--sky-bottom) 100%);
  }
  .flier__bands { position: absolute; left: 0; top: 0; }

  .brand {
    position: absolute; left: 0; top: 62px; width: 100%;
    text-align: center;
  }
  .brand__name {
    font-family: "Oswald", sans-serif; font-weight: 700;
    font-size: 62px; line-height: 1; letter-spacing: 1px;
    color: var(--teal); text-transform: uppercase;
  }
  .brand__tagline {
    display: inline-block; margin-top: 14px;
    padding: 3px 12px;
    background: var(--white);
    border: 3px solid var(--maroon);
    font-family: "Oswald", sans-serif; font-weight: 500;
    font-size: 20px; color: var(--maroon-dark); letter-spacing: .5px;
  }

  .performing {
    position: absolute; left: 0; top: 372px; width: 100%;
    text-align: center;
    font-size: 12px; letter-spacing: 4px; color: var(--white);
  }
  .performing__live { font-weight: 400; color: var(--teal); }
  .performing__label { font-weight: 600; }
  .performing::after {
    content: ""; display: block; width: 250px; height: 1px;
    margin: 7px auto 0; background: var(--teal);
  }

  .lineup {
    position: absolute; left: 0; top: 404px; width: 100%;
    display: flex; justify-content: center;
  }
  .lineup__col {
    list-style: none; width: 240px;
    font-family: "Roboto Slab", serif; font-weight: 800;
    font-size: 21px; line-height: 27px; color: var(--white);
  }
  .lineup__col--left { text-align: right; padding-right: 12px; }
  .lineup__col--right { text-align: left; padding-left: 12px; border-left: 2px solid var(--teal); }

  .dates {
    position: absolute; left: 70px; top: 622px; width: 400px; height: 62px;
    background: var(--teal); color: var(--maroon);
    display: flex; align-items: center; justify-content: center; gap: 12px;
  }
  .dates__range { font-family: "Montserrat", sans-serif; font-weight: 700; font-size: 34px; }
  .dates__range sup { font-size: 16px; }
  .dates__edition { font-size: 13px; font-weight: 600; align-self: flex-end; margin-bottom: 10px; }

  .venue {
    position: absolute; left: 0; top: 700px; width: 100%;
    text-align: center; color: var(--white); font-size: 14px; font-weight: 600;
  }
  .tickets {
    position: absolute; left: 0; bottom: 0; width: 100%; height: 34px;
    background: var(--teal); color: var(--maroon);
    display: flex; align-items: center; justify-content: center;
    font-size: 13px; font-weight: 600;
  }
  .tickets strong { font-weight: 700; margin-left: 4px; }
</style>
</head>
<body>
  <article class="flier">
    <div class="flier__scene" role="img" aria-label="Black and white photo of mountains under a cloudy sky"></div>

    <svg class="flier__bands" width="540" height="764" viewBox="0 0 540 764" aria-hidden="true">
      <polygon points="0,318 540,196 540,214 0,338" fill="var(--teal)"/>
      <polygon points="0,338 540,214 540,764 0,764" fill="var(--maroon)"/>
    </svg>

    <header class="brand">
      <div class="brand__name">Pass It Along</div>
      <div class="brand__tagline">COLORADO MUSIC FESTIVAL</div>
    </header>

    <p class="performing"><span class="performing__label">PERFORMING</span> <span class="performing__live">LIVE</span></p>

    <section class="lineup">
      <ul class="lineup__col lineup__col--left">
        <li>Dale Rivers Band</li>
        <li>Open Sky Orchestra</li>
        <li>Circuit Theory</li>
        <li>The Copper Pines</li>
        <li>K-Lo &amp; The Ridge</li>
        <li>Wapiti</li>
        <li>Fieldnotes</li>
      </ul>
      <ul class="lineup__col lineup__col--right">
        <li>Timberline Ensemble</li>
        <li>Blue Aspen</li>
        <li>Radiophonics</li>
        <li>Kaleidoscope</li>
        <li>Clear Signal</li>
        <li>Gold Creek Station</li>
        <li>Orbits</li>
      </ul>
    </section>

    <div class="dates">
      <span class="dates__range">May 11<sup>th</sup>-13<sup>th</sup>, 2018</span>
      <span class="dates__edition">6th Annual</span>
    </div>

    <p class="venue">Larkspur Yard 410 W. 52nd Ave. Denver, CO 80221</p>
    <p class="tickets">Tickets &amp; More Info @ <strong>www.passitalongfest.com</strong></p>
  </article>
</body>
</html>
```